Toprune redesign

Loreth Vance is a CPA specializing in consulting services to veterinarians nationwide. We need to revise the old generalist corporate identity to reflect her specialty. We need a revised card design with a photo of her and the registered trademark slogan The Paddock Ledger Coach(r). The slogan should appear on all materials. The ad needs to be revised with this photo and slogan. Go ahead and use the copy as is. I will revise it later.

```html
<!DOCTYPE html>
<html lang="en">
<head>
<meta charset="utf-8">
<title>Toprune — Envelope Set</title>
<link href="https://fonts.googleapis.com/css2?family=Arimo:wght@400;700&display=swap" rel="stylesheet">
<style>
  :root {
    --backdrop: #dcdcdc;
    --paper: #ffffff;
    --ink: #1e1e1e;
    --accent-red: #e3242b;
    --slogan-grey: #7a7a7a;
    --rule-grey: #555555;
    --corner-tone: #d4d4d4;
  }
  * { margin: 0; padding: 0; box-sizing: border-box; }
  html, body { width: 1200px; height: 1000px; overflow: hidden; }
  body {
    background: var(--backdrop);
    font-family: "Arimo", Arial, sans-serif;
    color: var(--ink);
    position: relative;
  }
  .envelope {
    position: absolute;
    background: var(--paper);
    overflow: hidden;
  }
  .envelope--front { left: 49px; top: 36px; width: 1102px; height: 487px; }
  .envelope--back  { left: 49px; top: 557px; width: 919px; height: 407px; }

  /* Corner accent area: soft tonal fill */
  .corner-accent {
    position: absolute; right: 0; bottom: 0;
    background: linear-gradient(135deg, rgba(212,212,212,0) 30%, var(--corner-tone) 100%);
  }
  .envelope--front .corner-accent { width: 218px; height: 178px; }
  .envelope--back .corner-accent { width: 182px; height: 178px; }

  /* Letterhead corner */
  .brand-mark {
    position: absolute; left: 30px; top: 40px;
    display: flex; align-items: center; gap: 8px;
  }
  .brand-mark__square { width: 14px; height: 14px; background: var(--ink); }
  .brand-mark__name { font-size: 20px; font-weight: 700; color: var(--ink); }
  .header-rule {
    position: absolute; left: 27px; top: 89px; width: 327px; height: 1px;
    background: #9a9a9a;
  }
  .sender { position: absolute; left: 172px; top: 36px; line-height: 1.2; }
  .sender__name { font-size: 13px; font-weight: 700; }
  .sender__title { font-size: 11.5px; }
  .sender__slogan { font-size: 11.5px; color: var(--accent-red); }
  .sender__address { margin-top: 22px; font-size: 10px; line-height: 1.25; }

  /* Back envelope */
  .memo-lines { position: absolute; left: 37px; top: 37px; width: 202px; }
  .memo-lines span {
    display: block; height: 1.5px; background: var(--rule-grey); margin-bottom: 18px;
  }
  .return-address { position: absolute; left: 460px; top: 200px; }
  .return-address__name { font-size: 15.5px; font-weight: 700; line-height: 20px; }
  .return-address__slogan { font-size: 14px; color: var(--slogan-grey); line-height: 19px; margin-bottom: 1px; }
  .return-address__line { font-size: 12.5px; line-height: 15px; }
</style>
</head>
<body>

<section class="envelope envelope--front">
  <div class="header-rule"></div>
  <div class="brand-mark">
    <span class="brand-mark__square"></span>
    <span class="brand-mark__name">Toprune</span>
  </div>
  <div class="sender">
    <p class="sender__name">Loreth Vance, CPA, PC</p>
    <p class="sender__title">Certified Public Accountants</p>
    <p class="sender__slogan">The Paddock Ledger Coach®</p>
    <p class="sender__address">1187 West Harrow Lane, Suite B<br>Mesa, AZ 85210</p>
  </div>
  <div class="corner-accent" role="img" aria-label="Decorative grey diagonal line pattern in the corner"></div>
</section>

<section class="envelope envelope--back">
  <div class="memo-lines"><span></span><span></span><span></span></div>
  <div class="return-address">
    <p class="return-address__name">Loreth Vance, CPA, PC</p>
    <p class="return-address__slogan">The Paddock Ledger Coach®</p>
    <p class="return-address__line">1187 West Harrow Lane, Suite B</p>
    <p class="return-address__line">Mesa, Arizona 85210</p>
  </div>
  <div class="corner-accent" role="img" aria-label="Decorative grey diagonal line pattern in the corner"></div>
</section>

</body>
</html>
```